Kovalen Spinal Care and Performance

We need new business cards, something more modern, clean. On the back of the card maybe a quote. The Dr. likes, “The doctor of the future will give no medicine, but will interest his patient in the care of the human frame, in diet and in the cause and prevention of disease.” - Walter Brisby. We are open to other suggestions. We are a chiropractic office.

```html
<!DOCTYPE html>
<html lang="en">
<head>
<meta charset="utf-8">
<title>Kovalen Spinal Care and Performance – Business Cards</title>
<link rel="stylesheet" href="https://fonts.googleapis.com/css2?family=Cinzel:wght@400;600&family=Open+Sans:wght@400;600;700&display=swap">
<style>
  :root {
    --purple: #5c2d6e;
    --purple-light: #9a72ab;
    --purple-deep: #56296a;
    --green: #8cab1e;
    --ink: #3a3a3a;
    --paper: #ffffff;
    --backdrop: #ecebe8;
  }
  * { box-sizing: border-box; margin: 0; padding: 0; }
  html, body { width: 1200px; height: 900px; overflow: hidden; }
  body { background: var(--backdrop); position: relative; font-family: "Open Sans", sans-serif; }

  .card {
    position: absolute;
    width: 520px;
    height: 300px;
    border-radius: 3px;
    overflow: hidden;
    box-shadow: 0 6px 18px rgba(0,0,0,0.18);
  }

  /* Back of card */
  .card-back {
    left: 70px; top: 170px;
    background: linear-gradient(180deg, var(--purple-light) 0%, var(--purple-deep) 100%);
    display: flex; flex-direction: column; align-items: center; justify-content: center;
    color: var(--paper); text-align: center; padding: 0 60px;
  }
  .quote {
    font-family: "Cinzel", serif;
    font-size: 16px;
    line-height: 1.35;
    letter-spacing: 0.3px;
  }
  .quote-author {
    font-weight: 700;
    font-size: 14px;
    margin-top: 4px;
  }

  /* Front of card */
  .card-front { left: 610px; top: 430px; background: var(--paper); }
  .front-wave { position: absolute; inset: 0; width: 100%; height: 100%; }

  .person { position: absolute; left: 34px; top: 40px; }
  .person-name {
    font-family: "Cinzel", serif; font-weight: 600;
    font-size: 20px; color: var(--purple); letter-spacing: 0.5px; line-height: 1.1;
  }
  .person-role { font-size: 14px; color: var(--ink); line-height: 1.2; }

  .brand {
    position: absolute; right: 30px; top: 36px; width: 200px;
    font-size: 17px; font-weight: 600; color: var(--purple); line-height: 1.25; text-align: left;
  }

  .contacts { position: absolute; left: 34px; top: 122px; list-style: none; font-size: 14px; color: var(--ink); line-height: 1.35; }
  .contacts li { display: flex; align-items: center; gap: 6px; }
  .contacts svg { width: 12px; height: 12px; flex: none; }
  .address { margin-top: 8px; display: block !important; }

  .website { position: absolute; right: 22px; top: 206px; color: var(--paper); font-size: 13px; }
</style>
</head>
<body>

  <section class="card card-back" aria-label="Back of business card">
    <p class="quote">“The doctor of the future will give no medicine but will interest his patient in the care of the human frame in diet and in the cause and prevention of disease.”</p>
    <p class="quote-author">-Walter Brisby</p>
  </section>

  <section class="card card-front" aria-label="Front of business card">
    <svg class="front-wave" viewBox="0 0 520 300" preserveAspectRatio="none" aria-hidden="true">
      <path d="M0,252 C170,268 330,205 470,140 L520,118 L520,300 L0,300 Z" fill="var(--green)"/>
      <path d="M0,274 C170,284 340,215 520,120 L520,300 L0,300 Z" fill="var(--paper)"/>
      <path d="M0,284 C170,292 350,220 520,128 L520,300 L0,300 Z" fill="var(--purple)"/>
    </svg>

    <div class="person">
      <p class="person-name">Daniel Hartwell</p>
      <p class="person-role">Managing Director</p>
    </div>

    <p class="brand">Kovalen Spinal Care and Performance</p>

    <ul class="contacts">
      <li>
        <svg viewBox="0 0 12 12"><path d="M1,4 Q6,0 11,4 L10,6 L8,5 L8,4 Q6,3 4,4 L4,5 L2,6 Z M3,7 H9 V10 H3 Z" fill="var(--green)"/></svg>
        044-555 018 246
      </li>
      <li>
        <svg viewBox="0 0 12 12"><rect x="3" y="0.5" width="6" height="11" rx="1" fill="none" stroke="var(--green)" stroke-width="1.5"/><circle cx="6" cy="9.5" r="0.8" fill="var(--green)"/></svg>
        044-555 018 246
      </li>
      <li>
        <svg viewBox="0 0 12 12"><rect x="0.5" y="2.5" width="11" height="7" fill="var(--green)"/><path d="M0.5,2.5 L6,7 L11.5,2.5" fill="none" stroke="#fff" stroke-width="1"/></svg>
        info@kovalenspine.com
      </li>
      <li class="address">12345, Address Goes Here<br>Country Name, 123456.</li>
    </ul>

    <p class="website">www.kovalenspine.com</p>
  </section>

</body>
</html>
```